Bref créative
Business Cards & Letterhead for a business that owns franchises
HARTWELL HOLDINGS GROUP
Professional
Gregory T. Pennock, Sr.
President & Co-Owner
3852 Fernhollow Bend, SE
Atlanta, GA
Gregory@HartHoldingsGroup.example
www.hartholdingsgroup.example
Our Logo? Be Creative!!
HARTWELL HOLDINGS GROUP LOGO

```html
<!DOCTYPE html>
<html lang="en">
<head>
<meta charset="utf-8">
<title>Hartwell Holdings Group — Business Cards</title>
<link rel="stylesheet" href="https://fonts.googleapis.com/css2?family=Cinzel:wght@500;600&family=Lato:wght@400;700&display=swap">
<style>
  :root {
    --bg: #e6e6e8;
    --card: #ffffff;
    --red: #c8202a;
    --red-dark: #9e1a21;
    --grey: #8a8c90;
    --grey-light: #d7d8da;
    --ink: #55575b;
    --white: #ffffff;
  }
  * { box-sizing: border-box; margin: 0; padding: 0; }
  html, body { width: 1200px; height: 646px; overflow: hidden; }
  body {
    background: var(--bg);
    font-family: "Lato", sans-serif;
    position: relative;
  }
  .card {
    position: absolute;
    top: 178px;
    width: 520px;
    height: 290px;
    background: var(--card);
    overflow: hidden;
    box-shadow: 0 6px 18px rgba(0,0,0,0.12);
  }
  .card--front { left: 50px; }
  .card--back { left: 630px; }
  .card__art { position: absolute; inset: 0; width: 100%; height: 100%; }

  .brand { display: flex; align-items: center; gap: 12px; }
  .brand__dot {
    width: 34px; height: 34px; border-radius: 50%;
    border: 3px solid var(--grey);
    flex: none;
  }
  .brand__name {
    font-family: "Cinzel", serif;
    font-weight: 600;
    color: var(--red);
    line-height: 1.15;
    letter-spacing: 0.06em;
  }

  /* front */
  .front__brand { position: absolute; left: 220px; top: 62px; }
  .front__brand .brand__name { font-size: 19px; width: 200px; }
  .front__person { position: absolute; left: 266px; top: 160px; }
  .person__name { font-family: "Lato", sans-serif; font-weight: 700; font-size: 16px; color: var(--red); }
  .person__title { font-size: 11px; color: var(--ink); margin-top: 3px; }
  .front__web { position: absolute; left: 220px; top: 226px; font-size: 10.5px; color: var(--grey); letter-spacing: 0.03em; }

  /* back */
  .back__brand { position: absolute; left: 38px; top: 112px; }
  .back__brand .brand__name { font-size: 17px; width: 170px; }
  .contacts {
    position: absolute; left: 328px; right: 12px; top: 78px;
    list-style: none; color: var(--white); font-size: 9.5px; line-height: 1.4;
  }
  .contacts li { display: flex; align-items: flex-start; gap: 7px; margin-bottom: 10px; }
  .contacts span { min-width: 0; overflow-wrap: anywhere; }
  .contacts svg { width: 11px; height: 11px; flex: none; margin-top: 1px; }
</style>
</head>
<body>

<section class="card card--front" aria-label="Business card front">
  <svg class="card__art" viewBox="0 0 520 290" aria-hidden="true">
    <circle cx="90" cy="150" r="120" fill="none" stroke="var(--grey-light)" stroke-width="10" opacity="0.6"/>
    <path d="M0 270 Q260 235 520 262 L520 290 L0 290 Z" fill="var(--grey-light)"/>
    <path d="M0 282 Q260 252 520 278 L520 290 L0 290 Z" fill="var(--red)"/>
  </svg>
  <div class="brand front__brand">
    <span class="brand__dot"></span>
    <span class="brand__name">HARTWELL HOLDINGS GROUP</span>
  </div>
  <div class="front__person">
    <p class="person__name">Gregory T. Pennock, Sr.</p>
    <p class="person__title">President &amp; Co-Owner</p>
  </div>
  <p class="front__web">www.hartholdingsgroup.example</p>
</section>

<section class="card card--back" aria-label="Business card back">
  <svg class="card__art" viewBox="0 0 520 290" aria-hidden="true">
    <path d="M300 0 Q250 145 300 290 L520 290 L520 0 Z" fill="var(--grey-light)"/>
    <path d="M316 0 Q268 145 316 290 L520 290 L520 0 Z" fill="var(--red)"/>
    <path d="M0 268 Q160 240 300 262 L300 290 L0 290 Z" fill="var(--grey-light)"/>
  </svg>
  <div class="brand back__brand">
    <span class="brand__dot"></span>
    <span class="brand__name">HARTWELL HOLDINGS GROUP</span>
  </div>
  <ul class="contacts">
    <li>
      <svg viewBox="0 0 12 12"><path d="M6 1a3.5 3.5 0 0 1 3.5 3.5C9.5 7.5 6 11 6 11S2.5 7.5 2.5 4.5A3.5 3.5 0 0 1 6 1z" fill="#fff"/><circle cx="6" cy="4.5" r="1.2" fill="var(--red)"/></svg>
      <span>3852 Fernhollow Bend, SE<br>Atlanta, GA</span>
    </li>
    <li>
      <svg viewBox="0 0 12 12"><path d="M3 1l2 2.5-1.2 1.2a7 7 0 0 0 3.5 3.5L8.5 7 11 9l-1.5 2C5 11 1 7 1 2.5z" fill="#fff"/></svg>
      <span>404-555-0142<br>678-555-0187</span>
    </li>
    <li>
      <svg viewBox="0 0 12 12"><rect x="1" y="2.5" width="10" height="7" fill="#fff"/><path d="M1 2.5l5 4 5-4" fill="none" stroke="var(--red)" stroke-width="1"/></svg>
      <span>Gregory@<wbr>HartHoldingsGroup.example</span>
    </li>
    <li>
      <svg viewBox="0 0 12 12"><circle cx="6" cy="6" r="4.8" fill="none" stroke="#fff" stroke-width="1.2"/><path d="M1.2 6h9.6M6 1.2c2.4 2.6 2.4 7 0 9.6M6 1.2c-2.4 2.6-2.4 7 0 9.6" fill="none" stroke="#fff" stroke-width="0.9"/></svg>
      <span>www.hartholdingsgroup.example</span>
    </li>
  </ul>
</section>

</body>
</html>
```